Post Lockdown Ortho Special

We are running a special for (Ortho) Braces/Clear Aligner (Quorventa), till July 31st 2020. Up to $2,000 off with free Consultation and Xrays.

We need a ad to run in different formats.

Maybe something with: what better time to get braces when you have to wear a mask all the time.

Trying to rebuild our business and get people in for free consultations.

```html
<!DOCTYPE html>
<html lang="en">
<head>
<meta charset="utf-8">
<title>Pinecrest Family Dentistry – Ortho Special</title>
<link rel="stylesheet" href="https://fonts.googleapis.com/css2?family=Cinzel:wght@500;700&family=Great+Vibes&family=Montserrat:wght@400;500;600;700;800&family=Raleway:wght@200;300&display=swap">
<style>
  :root {
    --purple: #5e3a9c;
    --purple-deep: #4b2c85;
    --gold: #d9b84a;
    --gold-light: #ecd27a;
    --ink: #1b1b1f;
    --grey: #8a8a93;
    --paper: #ffffff;
    --stage: #ecebef;
  }
  * { box-sizing: border-box; margin: 0; padding: 0; }
  html, body { width: 1200px; height: 800px; overflow: hidden; }
  body { background: var(--stage); font-family: "Montserrat", sans-serif; }

  .ad {
    position: absolute; left: 100px; top: 15px;
    width: 1000px; height: 770px;
    background: var(--paper); overflow: hidden;
    box-shadow: 0 6px 24px rgba(0,0,0,.12);
  }
  .ad-shapes { position: absolute; inset: 0; }

  .photo {
    position: absolute; left: 430px; top: 40px; width: 570px; height: 620px;
    background: radial-gradient(ellipse at 60% 55%, #f3dccb 0%, #e8c6ad 35%, #c99a7a 60%, #f4f1f3 85%);
  }

  .brand { position: absolute; left: 40px; top: 40px; display: flex; align-items: center; gap: 16px; }
  .brand-dot { width: 64px; height: 64px; border-radius: 50%; background: var(--purple); }
  .brand-name { font-family: "Cinzel", serif; font-weight: 700; color: var(--purple); font-size: 40px; line-height: 1; }
  .brand-sub { font-family: "Cinzel", serif; font-weight: 500; color: var(--purple); font-size: 14px; letter-spacing: 6px; margin-top: 4px; }
  .brand-doctor { font-family: "Cinzel", serif; font-weight: 500; color: var(--grey); font-size: 11px; letter-spacing: 2px; margin-top: 6px; }

  .offer-intro { position: absolute; left: 200px; top: 262px; color: #fff; font-size: 24px; font-weight: 500; }
  .offer-script { position: absolute; left: 30px; top: 270px; font-family: "Great Vibes", cursive; color: var(--gold); font-size: 120px; line-height: 1; }
  .offer-word { position: absolute; left: 190px; top: 370px; font-family: "Raleway", sans-serif; font-weight: 300; color: var(--gold); font-size: 100px; line-height: 1; }
  .offer-rule { position: absolute; left: 250px; top: 488px; }
  .offer-product { position: absolute; left: 36px; top: 505px; color: #fff; font-size: 22px; font-weight: 500; line-height: 1.25; }

  .badge {
    position: absolute; left: 450px; top: 400px; width: 220px; height: 220px; border-radius: 50%;
    background: #fff; border: 6px solid #cdbde6;
    display: flex; flex-direction: column; align-items: center; justify-content: center; text-align: center;
    color: var(--purple);
  }
  .badge-upto { font-size: 26px; font-weight: 700; }
  .badge-amount { font-size: 32px; font-weight: 800; color: var(--ink); line-height: 1.1; }
  .badge-extra { font-size: 15px; font-weight: 600; line-height: 1.2; margin-top: 4px; }
  .badge-rule { width: 40px; height: 3px; background: var(--purple); margin: 8px 0; }
  .badge-date { font-size: 15px; font-weight: 700; color: var(--ink); }
  .badge-date span { color: var(--purple); }

  .headline { position: absolute; left: 30px; top: 640px; font-size: 29px; font-weight: 800; line-height: 1.22; color: var(--ink); text-transform: uppercase; }
  .headline .accent { color: var(--purple); }

  .contact {
    position: absolute; left: 560px; top: 640px; width: 440px; height: 130px;
    background: var(--ink); color: #fff; padding: 16px 30px;
  }
  .contact-title { font-size: 20px; font-weight: 600; letter-spacing: .5px; }
  .contact-title b { font-weight: 800; }
  .contact-row { display: flex; align-items: center; gap: 12px; margin-top: 6px; }
  .contact-phone { color: var(--gold); font-size: 36px; font-weight: 800; line-height: 1.1; }
  .contact-email { font-size: 17px; font-weight: 500; }
</style>
</head>
<body>
<main class="ad">
  <div class="photo" role="img" aria-label="Photo of a smiling woman holding a clear aligner tray"></div>

  <svg class="ad-shapes" width="1000" height="770" viewBox="0 0 1000 770" aria-hidden="true">
    <path d="M0,232 L470,200 C420,320 398,440 418,570 C300,600 150,610 0,600 Z" fill="var(--purple)"/>
    <path d="M600,30 C460,160 380,420 470,570 C560,700 780,680 930,590" fill="none" stroke="var(--gold)" stroke-width="7"/>
    <path d="M0,612 C160,632 320,620 440,580" fill="none" stroke="var(--gold)" stroke-width="8"/>
  </svg>

  <div class="brand">
    <div class="brand-dot"></div>
    <div>
      <div class="brand-name">PINECREST</div>
      <div class="brand-sub">FAMILY DENTISTRY</div>
      <div class="brand-doctor">DR MARISA HOLLOWAY</div>
    </div>
  </div>

  <p class="offer-intro">We are running a</p>
  <p class="offer-script">Special</p>
  <p class="offer-word">offer</p>
  <svg class="offer-rule" width="120" height="14" viewBox="0 0 120 14" aria-hidden="true">
    <path d="M2,12 C40,2 80,2 118,6" fill="none" stroke="#fff" stroke-width="3"/>
  </svg>
  <p class="offer-product">(Ortho) Braces/Clear<br>Aligner (Quorventa)</p>

  <div class="badge">
    <div class="badge-upto">Up to</div>
    <div class="badge-amount">$2,000 off</div>
    <div class="badge-extra">with free Consultation<br>and Xrays</div>
    <div class="badge-rule"></div>
    <div class="badge-date">Till July 31st <span>2020</span></div>
  </div>

  <h1 class="headline">
    <span class="accent">What better time to</span><br>
    Get braces <span class="accent">when you have</span><br>
    To wear a mask <span class="accent">all the time.</span>
  </h1>

  <section class="contact">
    <p class="contact-title">CALL US FOR <b>FREE</b> CONSULTATION</p>
    <div class="contact-row">
      <svg width="26" height="26" viewBox="0 0 24 24" aria-hidden="true"><circle cx="12" cy="12" r="11" fill="none" stroke="#fff" stroke-width="1.5"/><path d="M8,6 L10,6 L11,9 L9.5,10 C10.3,11.8 12.2,13.7 14,14.5 L15,13 L18,14 L18,16 C18,17 17,18 16,18 C10.5,17.5 6.5,13.5 6,8 C6,7 7,6 8,6 Z" fill="#fff"/></svg>
      <span class="contact-phone">+1 555-014-2290</span>
    </div>
    <div class="contact-row">
      <svg width="22" height="16" viewBox="0 0 22 16" aria-hidden="true"><rect x="1" y="1" width="20" height="14" rx="1.5" fill="none" stroke="#fff" stroke-width="1.6"/><path d="M1.5,2 L11,9 L20.5,2" fill="none" stroke="#fff" stroke-width="1.6"/></svg>
      <span class="contact-email">marisahollowaydds@mailbox.com</span>
    </div>
  </section>
</main>
</body>
</html>
```